Design a Website Mockup and a Logo for TotsCoverly

Hi,
I need a logo and website design for a new site - TotsCoverly.com.au.

What the site does:
When a teacher is sick, they log into the site and flag that they need to be replaced for the day. Someone from the kindergarten/school authorises it, and the job is sent to replacement teachers. They accept the job, and are notified whether they are successful or not. If successful they come to work.

I need all pages to be designed, but will pick the winner based on the logo, homepage, and a calendar. I'll then work with the winner to finalise the design of a features page (based on the homepage), login screen and data entry pages (included within the contest prize of $500).
The calendar is used by the kindergarten/school so that they can easily see which days a teacher will be absent, which replacement jobs have been advertised, which jobs have been applied for, and which jobs they have filled. I'm thinking it should just be a different colour for different statuses, but it doesn't have to be.
There is a separate calendar for teachers, so that they can see when and where they have been booked to work.
The closest comparison site is www.StaffPivot.com.au. This is the closest in terms of app functionality and what the product does - this is not what I want the site design or the logo to look like.

For the homepage design I am looking for something similar to [url removed, login to view], although not necessarily the same colour scheme. The attached word document has the text that goes in the different bands of the layout.

Logo design - I'm looking for something simple and modern, in a vector format. Can be either abstract or pictorial. Not looking for a word art type logo, or something that is just letters K and or R (so not a Pagebind type logo), as if this product works well for kindergartens, I might expand into other areas where the name or letters won't work.
The logo also needs to be suitable for an zuFone app icon.
Some logos I like - GraphPulse, ZipTalk, Vorn, Sonara, Gigsmith, Plumb, Tunelo.
What I don't want - anything like Moonbrew, Velmora 2019, Tessa Varlo, Bramwick, Veltra.

```html
<!DOCTYPE html>
<html lang="en">
<head>
<meta charset="utf-8">
<title>TotsCoverly — Kindergarten Relief</title>
<link href="https://fonts.googleapis.com/css2?family=Jost:wght@300;400;500;600;700&family=Parisienne&family=Open+Sans:wght@400&display=swap" rel="stylesheet">
<style>
:root{
  --ink:#1d1d1d;
  --muted:#666;
  --white:#fff;
  --yellow:#e6ec0c;
  --blue:#0f6fe6;
  --teal:#4cb8b0;
  --teal-dark:#1f6e67;
  --mint:#5fd3c5;
  --band-grey:#ededed;
  --footer:#f3f3f3;
  --laptop:#5b5b5b;
  --laptop-dark:#333;
}
*{margin:0;padding:0;box-sizing:border-box}
html,body{width:866px;height:1200px;overflow:hidden;background:var(--white)}
body{position:relative;font-family:'Jost',sans-serif;color:var(--ink)}
.abs{position:absolute;white-space:nowrap}

/* hero */
.hero{left:0;top:0;width:866px;height:309px;overflow:hidden}
.hero-photo{position:absolute;inset:0;background:
  radial-gradient(ellipse 200px 170px at 200px 170px,#7a5a48 0%,rgba(90,50,70,0) 100%),
  linear-gradient(100deg,#5a2a55 0%,#3b2a33 35%,#2b2622 60%,#4a3a2c 85%,#3c4a2a 100%)}
.hero-shade{position:absolute;inset:0;background:rgba(0,0,0,.28)}
.nav{left:0;top:0;width:866px;height:32px;border-bottom:1px solid rgba(255,255,255,.25)}
.brand{left:150px;top:6px;display:flex;align-items:center;gap:5px;color:var(--white);font-size:19px;font-weight:500;line-height:1}
.brand-mark{width:12px;height:12px;background:var(--yellow)}
.nav-link{top:13px;color:var(--white);font-size:6.6px;font-weight:500;line-height:1}
.nav-btn{top:10px;height:15px;border-radius:2px;font-size:6.4px;font-weight:700;display:flex;align-items:center;justify-content:center}
.nav-btn.signup{left:635px;width:37px;background:var(--yellow);color:var(--ink)}
.nav-btn.login{left:677px;width:37px;border:1px solid rgba(255,255,255,.8);color:var(--white)}
.hero-title{left:300px;top:128px;width:470px;text-align:center;color:var(--white);font-size:28.5px;font-weight:600;line-height:1.1}
.hero-sub{left:436px;top:172px;color:var(--white);font-weight:300;display:flex;align-items:flex-start;line-height:1}
.hero-sub .word{font-size:21px}
.hero-sub .teachers{margin-top:8px}
.hero-sub .amp{font-size:46px;margin:0 5px 0 4px;font-weight:300}
.hero-sub .assist{margin-top:29px}
.hero-tag{left:590px;top:244px;color:var(--mint);font-family:'Parisienne',cursive;font-size:19px}
.dots{left:418px;top:294px;display:flex;gap:2px}
.dots span{width:4px;height:4px;border-radius:50%;background:#c9c9c9}

/* welcome */
.welcome-title{left:0;top:329px;width:866px;text-align:center;font-size:15px;font-weight:400}
.welcome-copy{left:0;top:360px;width:866px;text-align:center;font-family:'Open Sans',sans-serif;font-size:9.2px;line-height:15.5px;color:var(--muted)}

/* demo */
.demo-band{left:0;top:438px;width:866px;height:257px;background:var(--band-grey)}
.laptop{left:258px;top:452px}
.demo-callout{left:615px;top:536px;width:50px;height:50px;border-radius:50%;background:var(--yellow);display:flex;align-items:center;justify-content:center;text-align:center;font-family:'Parisienne',cursive;font-size:10.5px;line-height:10px;color:var(--ink)}

/* more */
.more{left:0;top:695px;width:866px;height:272px;overflow:hidden}
.more-photo{position:absolute;inset:0;background:
  radial-gradient(ellipse 180px 200px at 230px 130px,#3e342c 0%,rgba(0,0,0,0) 100%),
  radial-gradient(ellipse 200px 200px at 640px 160px,#3b3a44 0%,rgba(0,0,0,0) 100%),
  linear-gradient(90deg,#151412,#2a2622 50%,#1c1c1e)}
.more-title{left:0;top:38px;width:866px;text-align:center;color:var(--white);font-size:28px;font-weight:500}
.choice{top:140px;width:160px;height:37px;border-radius:2px;display:flex;align-items:center;justify-content:center;font-size:13.5px;font-weight:400}
.choice.teacher{left:283px;background:var(--blue);color:var(--white)}
.choice.kinder{left:452px;background:var(--yellow);color:var(--ink)}

/* start */
.start{left:0;top:967px;width:866px;height:130px;background:var(--teal)}
.start-text{left:258px;top:50px;color:var(--white);font-size:22px;font-weight:300;line-height:1.2}
.start-btn{left:459px;top:49px;width:130px;height:29px;background:var(--teal-dark);border-radius:2px;color:var(--white);font-size:11px;font-weight:400;letter-spacing:.3px;display:flex;align-items:center;justify-content:center}

/* footer */
.footer{left:0;top:1097px;width:866px;height:103px;background:var(--footer)}
.footer-col{top:12px;width:130px}
.footer-col h4{font-size:8px;font-weight:400;margin-bottom:6px;color:var(--ink)}
.footer-col a{display:block;font-family:'Open Sans',sans-serif;font-size:6.5px;color:#555;text-decoration:none;padding:2px 0 4px;border-bottom:1px solid #dcdcdc;margin-bottom:2px}
.copyright{left:0;top:90px;width:866px;text-align:center;font-family:'Open Sans',sans-serif;font-size:5px;color:#999}
</style>
</head>
<body>

<section class="abs hero">
  <div class="hero-photo" role="img" aria-label="Photo of a smiling child in a kindergarten classroom, softly blurred"></div>
  <div class="hero-shade"></div>
  <nav class="abs nav">
    <div class="abs brand"><span class="brand-mark"></span>TotsCoverly</div>
    <span class="abs nav-link" style="left:496px">FOR TEACHERS</span>
    <span class="abs nav-link" style="left:554px">FOR KINDERGARTENS</span>
    <span class="abs nav-btn signup">SIGN UP</span>
    <span class="abs nav-btn login">LOGIN</span>
  </nav>
  <h1 class="abs hero-title">KINDERGARTEN RELIEF</h1>
  <div class="abs hero-sub"><span class="word teachers">Teachers</span><span class="amp">&amp;</span><span class="word assist">Assistants</span></div>
  <div class="abs hero-tag">Fast and Easy</div>
  <div class="abs dots"><span></span><span></span><span></span></div>
</section>

<h2 class="abs welcome-title">Welcome to the Easiest way to Find Relief staff for Kindergartens.</h2>
<p class="abs welcome-copy">TotsCoverly was created to take the hassle and expense out of finding last minute (or advance) replacements when your teachers or<br>assistants are sick, on leave or on training.For teachers and assistants, it makes it easy to get and manage bookings, so you can<br>worry about teaching, and not constantly looking for work.</p>

<section class="abs demo-band"></section>
<svg class="abs laptop" width="360" height="230" viewBox="0 0 360 230" role="img" aria-label="Laptop showing the TotsCoverly demo video">
  <rect x="24" y="0" width="312" height="215" rx="10" fill="var(--laptop)"/>
  <rect x="38" y="15" width="284" height="191" fill="#8a8a8a"/>
  <circle cx="180" cy="7" r="2.5" fill="#2a2a2a"/>
  <path d="M0 213 H360 V220 Q360 228 350 228 H10 Q0 228 0 220 Z" fill="var(--laptop-dark)"/>
  <rect x="150" y="213" width="60" height="5" fill="#6a6a6a"/>
  <text x="180" y="116" text-anchor="middle" font-family="Jost, sans-serif" font-size="24" fill="#333">TotsCoverly</text>
  <rect x="146" y="94" width="58" height="34" fill="rgba(200,200,200,.75)"/>
  <path d="M168 101 L186 111 L168 121 Z" fill="var(--white)"/>
</svg>
<div class="abs demo-callout">Watch<br>demo now</div>
<svg class="abs" style="left:594px;top:563px" width="22" height="20" viewBox="0 0 22 20" aria-hidden="true">
  <path d="M20 2 Q12 4 4 16" stroke="#c8cc10" stroke-width="1.2" fill="none"/>
  <path d="M3 11 L4 16 L9 15" stroke="#c8cc10" stroke-width="1.2" fill="none"/>
</svg>

<section class="abs more">
  <div class="more-photo" role="img" aria-label="Blurred photo of a teacher helping a child draw at a table"></div>
  <h2 class="abs more-title">Want to know More?</h2>
  <a class="abs choice teacher">I’m a Teacher or Assistant</a>
  <a class="abs choice kinder">I’m a kindergarten</a>
</section>

<section class="abs start">
  <span class="abs start-text">Want to Get Started?</span>
  <a class="abs start-btn">CREATE MY PROFILE</a>
</section>

<footer class="abs footer">
  <div class="abs footer-col" style="left:151px"><h4>WHO WE ARE</h4><a>About us</a><a>Terms of Services</a><a>Privacy Policy</a></div>
  <div class="abs footer-col" style="left:296px"><h4>OUR SERVICES</h4><a>For Kindergartens</a><a>For Teachers</a><a>For Assistants</a></div>
  <div class="abs footer-col" style="left:440px"><h4>RESOURCES</h4><a>Support</a><a>FAQ</a><a>Contact us</a></div>
  <div class="abs footer-col" style="left:585px"><h4>SAY HELLO</h4><a>Blog</a><a>Chirpline</a><a>Pagebind</a></div>
  <div class="abs copyright">Copyright 2015 · All rights reserved</div>
</footer>

</body>
</html>
```